Maple Ridge business card design

Card needs to include the following text/items:
Company Logo
Tobin Marsh
Phone # - 555-318-7642
service@mapleridgelandscaping.example
Lawn & landscape maintenance services

```html
<!DOCTYPE html>
<html lang="en">
<head>
<meta charset="utf-8">
<title>Maple Ridge Landscaping – Business Card</title>
<link rel="stylesheet" href="https://fonts.googleapis.com/css2?family=Cinzel:wght@600;700&family=Open+Sans:wght@400&display=swap">
<style>
  :root {
    --backdrop: #e3e3e3;
    --forest: #0d4526;
    --olive: #86993d;
    --paper: #f4f4f4;
    --ink: #1c1c1c;
    --white: #ffffff;
    --mark-top: #5fb8d8;
    --mark-bottom: #2f6b34;
  }
  * { margin: 0; padding: 0; box-sizing: border-box; }
  html, body { width: 1200px; height: 960px; overflow: hidden; }
  body { background: var(--backdrop); position: relative; font-family: "Open Sans", Arial, sans-serif; }

  .card { position: absolute; left: 300px; width: 610px; height: 349px; overflow: hidden; }

  .brand-title { display: block; font-family: "Cinzel", Georgia, serif; font-weight: 600; white-space: nowrap; }
  .brand-sub { display: block; font-family: "Cinzel", Georgia, serif; font-weight: 600; white-space: nowrap; }

  /* Front */
  .card-front { top: 106px; background: var(--forest); }
  .front-mark {
    position: absolute; left: 219px; top: 56px; width: 172px; height: 172px;
    border-radius: 50%; border: 3px solid var(--olive);
    background: linear-gradient(var(--mark-top), var(--mark-bottom));
  }
  .front-name { position: absolute; left: 0; right: 0; top: 234px; text-align: center; color: var(--white); }
  .front-name .brand-title { font-size: 40px; line-height: 42px; }
  .front-name .brand-sub { font-size: 18px; line-height: 22px; letter-spacing: 12px; padding-left: 12px; }

  /* Back */
  .card-back { top: 508px; background: var(--paper); }
  .back-name { position: absolute; left: 47px; top: 44px; color: var(--forest); }
  .back-name .brand-title { font-size: 37px; line-height: 38px; }
  .back-name .brand-sub { font-size: 17px; line-height: 20px; letter-spacing: 9.5px; }
  .back-mark {
    position: absolute; left: 325px; top: 8px; width: 340px; height: 340px;
    border-radius: 50%; border: 4px solid var(--olive);
    background: linear-gradient(var(--mark-top), var(--mark-bottom));
  }
  .person { position: absolute; left: 47px; top: 158px; }
  .person-name {
    font-family: "Cinzel", Georgia, serif; font-weight: 600; color: var(--forest);
    font-size: 24px; line-height: 28px; letter-spacing: 0.5px;
  }
  .person-role { font-size: 14.5px; color: var(--ink); margin-top: 2px; }
  .divider { position: absolute; left: 47px; top: 217px; width: 280px; height: 2px; background: var(--olive); }
  .contacts { position: absolute; left: 47px; top: 233px; list-style: none; }
  .contacts li { display: flex; align-items: center; gap: 6px; font-size: 13px; line-height: 20.5px; color: var(--ink); white-space: nowrap; }
  .contacts svg { width: 13px; height: 13px; fill: var(--forest); flex: none; }
  .tagline-band {
    position: absolute; left: 0; right: 0; bottom: 0; height: 35px; background: var(--forest);
    display: flex; align-items: center; justify-content: center;
    font-family: "Cinzel", Georgia, serif; font-weight: 600; color: var(--white); font-size: 17px; letter-spacing: 0.5px;
  }
</style>
</head>
<body>
  <section class="card card-front">
    <div class="front-mark" role="img" aria-label="Company mark area"></div>
    <div class="front-name"><span class="brand-title">Maple Ridge</span><span class="brand-sub">Landscaping</span></div>
  </section>

  <section class="card card-back">
    <div class="back-name"><span class="brand-title">Maple Ridge</span><span class="brand-sub">Landscaping</span></div>
    <div class="back-mark" role="img" aria-label="Company mark area"></div>
    <div class="person">
      <div class="person-name">Tobin Marsh</div>
      <div class="person-role">Owner</div>
    </div>
    <div class="divider"></div>
    <ul class="contacts">
      <li><svg viewBox="0 0 24 24"><path d="M6.6 10.8a15.1 15.1 0 0 0 6.6 6.6l2.2-2.2a1 1 0 0 1 1-.25 11.4 11.4 0 0 0 3.6.6 1 1 0 0 1 1 1V20a1 1 0 0 1-1 1A17 17 0 0 1 3 4a1 1 0 0 1 1-1h3.5a1 1 0 0 1 1 1c0 1.25.2 2.45.6 3.6a1 1 0 0 1-.25 1z"/></svg>555-318-7642</li>
      <li><svg viewBox="0 0 24 24"><path d="M2 4h20v16H2zm2 2v.5l8 5 8-5V6zm0 2.8V18h16V8.8l-8 5z"/></svg>service@mapleridgelandscaping.example</li>
      <li><svg viewBox="0 0 24 24"><path d="M12 2a10 10 0 1 0 0 20 10 10 0 0 0 0-20zm6.9 6h-3a15 15 0 0 0-1.3-3.9A8 8 0 0 1 18.9 8zM12 4c.8 1.2 1.5 2.5 1.9 4h-3.8c.4-1.5 1.100-2.8 1.9-4zM4.3 14a8 8 0 0 1 0-4h3.4a16 16 0 0 0 0 4zm.8 2h3a15 15 0 0 0 1.3 3.9A8 8 0 0 1 5.1 16zm3-8h-3a8 8 0 0 1 4.3-3.9A15 15 0 0 0 8.1 8zM12 20c-.8-1.2-1.5-2.5-1.9-4h3.8c-.4 1.5-1.1 2.8-1.900 4zm2.3-6H9.7a14 14 0 0 1 0-4h4.6a14 14 0 0 1 0 4zm.3 5.9a15 15 0 0 0 1.3-3.9h3a8 8 0 0 1-4.3 3.9zM16.3 14a16 16 0 0 0 0-4h3.4a8 8 0 0 1 0 4z"/></svg>www.mapleridgelandscaping.example</li>
    </ul>
    <div class="tagline-band">Lawn &amp; Landscape Maintenance Services</div>
  </section>
</body>
</html>
```